Lottie's Clam Shack Website

We are looking to create an official website for our seafood restaurant with the following specifications:
Design style: modern, street, industrial and neon aesthetic; primary color palette: black, white and red.
Prominent placement for online ordering on the homepage.
Feature our current single location, plus a dedicated section/page for our upcoming second restaurant opening.
The site must be fully ADA compliant.
Full social media integration with linked profiles.
Include a floating contact/comment widget for customer inquiries and messages.
Mobile-first responsive design, optimized primarily for mobile users.
Preferred platform: Squarespace. Alternative option: Wix, for simple future self-maintenance and content updates.
The design should have unique personality and creative styling. We prefer a custom, distinctive look rather than a generic, rigid and standard template layout.

our ins:@lottiesclamshack

"snagashrimpwx.com" this is another restraunt like us, and we like their web, but please dont make us the same like theirs.

```html
<!DOCTYPE html>
<html lang="en">
<head>
<meta charset="utf-8">
<title>Lottie's Clam Shack</title>
<link href="https://fonts.googleapis.com/css2?family=Archivo:wght@800;900&family=Poppins:wght@400;500;600;700&display=swap" rel="stylesheet">
<style>
:root{
  --red:#e41e26;
  --ink:#111111;
  --text:#333333;
  --white:#ffffff;
  --dark:#0d0b0a;
  --line:#8a8a8a;
  --gold:#f5b400;
}
*{box-sizing:border-box;margin:0;padding:0}
html,body{width:1200px;height:4240px;overflow:hidden}
body{position:relative;background:var(--white);font-family:"Poppins",sans-serif;color:var(--text)}
.abs{position:absolute}
.btn{position:absolute;display:flex;align-items:center;justify-content:center;background:var(--red);color:var(--white);font-weight:600;border-radius:30px;text-transform:uppercase}
.title{font-family:"Archivo",sans-serif;font-weight:800;color:var(--red);text-transform:uppercase;letter-spacing:1px}
.rule{position:absolute;height:4px;width:62px;background:var(--line);border-radius:2px}
.rule::before{content:"";position:absolute;left:0;top:-2px;width:8px;height:8px;border-radius:50%;background:var(--line)}

/* header */
.header{position:absolute;left:0;top:0;width:1200px;height:151px;background:var(--white)}
.brand{position:absolute;display:flex;align-items:center;gap:12px;font-family:"Poppins",sans-serif;font-weight:700;color:var(--ink);white-space:nowrap}
.brand .mark{border-radius:50%;background:var(--red);flex:none}
.contact-line{position:absolute;display:flex;align-items:center;gap:10px;font-size:15px;font-weight:500;color:var(--ink)}
.ico{width:28px;height:28px;border-radius:50%;background:var(--red);display:flex;align-items:center;justify-content:center}
.nav{position:absolute;left:490px;top:85px;display:flex;gap:16px;font-size:13px;color:var(--ink);text-transform:uppercase}
.nav .active{font-weight:600}

/* hero */
.hero{position:absolute;left:0;top:151px;width:1200px;height:611px;background:linear-gradient(120deg,#2a1d16,#120c09 60%,#1d120c)}
.hero-photo{position:absolute;left:0;top:0;width:642px;height:611px;border-radius:0 120px 0 0;background:radial-gradient(circle at 45% 45%,#b8401f,#5a2415 45%,#1c1c1f 85%)}
.hero-copy{position:absolute;left:640px;top:140px;width:535px;text-align:center;color:var(--white)}
.hero-copy .kicker{font-size:15px;font-weight:600;letter-spacing:.5px}
.hero-copy h1{font-family:"Archivo",sans-serif;font-weight:900;color:var(--red);line-height:1;margin-top:14px}
.hero-copy h1 .l1{display:block;font-size:82px}
.hero-copy h1 .l2{display:block;font-size:60px;margin-top:6px}
.hero-copy p{font-size:14px;line-height:24px;margin-top:22px}

/* about & touch */
.copy h3{font-size:21px;font-weight:500;color:var(--ink);line-height:31px}
.copy p{font-size:13px;line-height:24px;text-align:justify;margin-top:12px}
.about-photo{position:absolute;left:563px;top:772px;width:637px;height:647px;border-radius:110px 0 0 110px;background:radial-gradient(circle at 50% 40%,#d86a2a,#8a3b18 45%,#3b4d45 75%,#9bb8b8)}
.touch-photo{position:absolute;left:0;top:3128px;width:556px;height:646px;border-radius:0 100px 100px 0;background:radial-gradient(circle at 45% 45%,#3a1208,#6b2410 40%,#c7c0b8 80%)}

/* menus */
.menus{position:absolute;left:0;top:1430px;width:1200px;height:1678px}
.menus-bg{position:absolute;inset:0;background:radial-gradient(ellipse at 50% 40%,#2b1a12,#0b0908 75%)}
.tabs{position:absolute;left:71px;top:1713px;width:1065px;height:42px;overflow:hidden}
.tab{position:absolute;top:0;height:42px;border:2px solid var(--white);border-radius:4px;color:var(--white);font-size:12.5px;font-weight:600;display:flex;align-items:center;justify-content:center;text-transform:uppercase;white-space:nowrap}
.tab.on{background:var(--red);border-color:var(--red)}
.card{position:absolute;width:316px;height:501px;border:1px solid #4a4440;background:rgba(0,0,0,.35);text-align:center;color:var(--white)}
.card .dish{position:absolute;left:24px;top:24px;width:268px;height:262px;border:2px solid #ddd}
.card .fav{position:absolute;right:16px;top:16px;width:32px;height:32px;border-radius:50%;background:rgba(255,255,255,.8);display:flex;align-items:center;justify-content:center}
.card h4{position:absolute;left:0;right:0;top:311px;font-size:21px;font-weight:500}
.card .price{position:absolute;left:0;right:0;top:343px;font-size:33px;font-weight:700}
.card .stars{position:absolute;left:0;right:0;top:398px;font-size:19px;color:var(--gold);letter-spacing:1px}
.card .add{position:absolute;left:96px;top:435px;width:123px;height:38px;background:var(--red);border-radius:3px;font-size:12px;font-weight:600;display:flex;align-items:center;justify-content:center}
.dots{position:absolute;top:2912px;left:582px;display:flex;gap:5px}
.dots span{width:10px;height:10px;border-radius:50%;border:1.5px solid var(--white)}
.dots span.on{background:var(--white)}

/* footer */
.footer{position:absolute;left:0;top:3799px;width:1200px;height:441px;background:linear-gradient(180deg,#1a1412,#0a0807);color:var(--white)}
.fh{position:absolute;font-size:21px;font-weight:600;text-transform:uppercase}
.fh::after{content:"";position:absolute;left:0;top:38px;width:60px;height:2px;background:var(--line)}
.flinks{position:absolute;left:306px;top:4030px;list-style:none;font-size:14px}
.flinks li{height:32.5px;display:flex;align-items:center;gap:14px}
.flinks li::before{content:"";width:8px;height:8px;border-radius:50%;background:var(--white);box-shadow:0 0 0 2px #777}
.fitem{position:absolute;display:flex;align-items:center;gap:16px;font-size:14px;line-height:25px}
.fitem .ico{width:34px;height:34px;background:var(--white);flex:none}
.social{position:absolute;left:94px;top:4120px;display:flex;gap:6px}
.social span{width:31px;height:31px;border-radius:50%;background:var(--white)}
.input{position:absolute;left:813px;top:4056px;width:295px;height:44px;background:var(--white);border-radius:4px;color:#999;font-size:13px;display:flex;align-items:center;padding-left:16px}
.signup{position:absolute;left:815px;top:4120px;width:120px;height:36px;background:var(--white);color:var(--ink);border-radius:4px;font-size:12px;font-weight:700;display:flex;align-items:center;justify-content:center}
.next-spot{position:absolute;left:813px;top:4172px;font-size:13px;color:var(--white)}
.next-spot b{color:var(--red);font-weight:600}
.fbase{position:absolute;left:66px;top:4230px;width:1068px;height:1px;background:#555}
.chat-widget{position:absolute;left:1130px;top:4160px;width:52px;height:52px;border-radius:50%;background:var(--red);display:flex;align-items:center;justify-content:center;box-shadow:0 4px 12px rgba(0,0,0,.5)}
</style>
</head>
<body>

<header class="header">
  <div class="brand" style="left:60px;top:48px;font-size:26px">
    <span class="mark" style="width:44px;height:44px"></span>Lottie's Clam Shack
  </div>
  <div class="contact-line" style="left:745px;top:29px">
    <span class="ico"><svg width="14" height="14" viewBox="0 0 24 24"><path fill="#fff" d="M6.6 10.8a15 15 0 0 0 6.6 6.6l2.2-2.2c.3-.3.7-.4 1-.2 1.1.4 2.3.6 3.6.6.6 0 1 .4 1 1V20c0 .6-.4 1-1 1A17 17 0 0 1 3 4c0-.6.4-1 1-1h3.5c.6 0 1 .4 1 1 0 1.3.2 2.5.6 3.6.1.3 0 .7-.2 1z"/></svg></span>555-014-0273
  </div>
  <div class="contact-line" style="left:896px;top:29px">
    <span class="ico"><svg width="14" height="14" viewBox="0 0 24 24"><path fill="#fff" d="M3 6h18v12H3z"/><path d="M3 6l9 7 9-7" stroke="#e41e26" stroke-width="2" fill="none"/></svg></span>info@companyname.com
  </div>
  <nav class="nav">
    <span class="active">Home</span><span>Online Ordering</span><span>Menu</span><span>Membership</span><span>Weekday Specials</span>
  </nav>
  <div class="btn" style="left:996px;top:76px;width:138px;height:40px;font-size:12px">Contact Us</div>
</header>

<section class="hero">
  <div class="hero-photo" role="img" aria-label="Photo of a grilled lobster platter with herbs on a dark plate"></div>
  <div class="hero-copy">
    <div class="kicker">WELCOME TO</div>
    <h1><span class="l1">LOTTIE'S</span><span class="l2">CLAM SHACK</span></h1>
    <p>Lorem ipsum dolor sit amet, consectetur adipiscing elit,<br>sed do eiusmod tempor incididunt ut labore.</p>
  </div>
  <div class="btn" style="left:820px;top:423px;width:174px;height:43px;font-size:14px">Contact Us</div>
</section>

<section>
  <h2 class="title abs" style="left:67px;top:895px;font-size:50px">About Us</h2>
  <div class="rule" style="left:67px;top:964px"></div>
  <div class="copy abs" style="left:67px;top:991px;width:465px">
    <h3>Lorem ipsum dolor sit amet, consectetur adipiscing elit,</h3>
    <p>sed do eiusmod tempor incididunt ut labore et dolore magna aliqua. Ut enim ad minim veniam, quis nostrud exercitation ullamco laboris nisi ut aliquip ex ea commodo consequat. Duis aute irure dolor in reprehenderit in voluptate velit esse cillum dolore eu fugiat nulla pariatur. Excepteur sint occaecat cupidatat non proident, sunt in culpa qui officia deserunt mollit anim id est laborum.</p>
  </div>
  <div class="btn" style="left:67px;top:1236px;width:129px;height:43px;font-size:13px">Read More</div>
  <div class="about-photo" role="img" aria-label="Photo of a whole crab stir-fried with peppers in a blue bowl"></div>
</section>

<section class="menus">
  <div class="menus-bg" role="img" aria-label="Dim background photo of a seafood table"></div>
</section>
<h2 class="title abs" style="left:0;width:1200px;text-align:center;top:1570px;font-size:52px">Our Menus</h2>
<div class="rule" style="left:569px;top:1641px"></div>
<div class="tabs">
  <div class="tab on" style="left:0;width:192px">Fried Seafood Baskets</div>
  <div class="tab" style="left:206px;width:110px">Appetizer</div>
  <div class="tab" style="left:327px;width:81px">Sides</div>
  <div class="tab" style="left:419px;width:89px">Dessert</div>
  <div class="tab" style="left:520px;width:90px">Drinks</div>
  <div class="tab" style="left:622px;width:163px">Seafood by the LB</div>
  <div class="tab" style="left:798px;width:186px">Choose Your Flavor</div>
  <div class="tab" style="left:996px;width:110px;justify-content:flex-start;padding-left:12px">Spice It Up</div>
</div>

<div class="card" style="left:100px;top:1820px"><div class="dish" role="img" aria-label="Photo of fried oysters with salad" style="background:radial-gradient(circle,#c98a4a,#6f8a4a 60%,#777)"></div><div class="fav"><svg width="16" height="16" viewBox="0 0 24 24"><path fill="#999" d="M12 21l-1.4-1.3C5.4 15 2 12 2 8.3 2 5.4 4.4 3 7.3 3c1.7 0 3.3.8 4.7 2 1.4-1.2 3-2 4.7-2C19.6 3 22 5.4 22 8.3c0 3.7-3.4 6.7-8.6 11.4z"/></svg></div><h4>Fried Oysters</h4><div class="price">$13</div><div class="stars">★★★★★</div><div class="add">ADD TO CART</div></div>
<div class="card" style="left:438px;top:1820px"><div class="dish" role="img" aria-label="Photo of fried shrimp on a plate" style="background:radial-gradient(circle,#e07a2a,#8a3a1a 60%,#2a2220)"></div><div class="fav"><svg width="16" height="16" viewBox="0 0 24 24"><path fill="#999" d="M12 21l-1.4-1.3C5.4 15 2 12 2 8.3 2 5.4 4.4 3 7.3 3c1.7 0 3.3.8 4.7 2 1.4-1.2 3-2 4.7-2C19.6 3 22 5.4 22 8.3c0 3.7-3.4 6.7-8.6 11.4z"/></svg></div><h4>Fried Shrimp</h4><div class="price">$15</div><div class="stars">★★★★★</div><div class="add">ADD TO CART</div></div>
<div class="card" style="left:777px;top:1820px"><div class="dish" role="img" aria-label="Photo of fried catfish with lemon" style="background:radial-gradient(circle,#c08040,#d9d4cc 55%,#555)"></div><div class="fav"><svg width="16" height="16" viewBox="0 0 24 24"><path fill="#999" d="M12 21l-1.4-1.3C5.4 15 2 12 2 8.3 2 5.4 4.4 3 7.3 3c1.7 0 3.3.8 4.7 2 1.4-1.2 3-2 4.7-2C19.6 3 22 5.4 22 8.3c0 3.7-3.4 6.7-8.6 11.4z"/></svg></div><h4>Fried Catfish</h4><div class="price">$13</div><div class="stars">★★★★★</div><div class="add">ADD TO CART</div></div>
<div class="card" style="left:100px;top:2347px"><div class="dish" role="img" aria-label="Photo of fried calamari rings with dip" style="background:radial-gradient(circle,#e0a040,#b07030 55%,#888)"></div><div class="fav"><svg width="16" height="16" viewBox="0 0 24 24"><path fill="#999" d="M12 21l-1.4-1.3C5.4 15 2 12 2 8.3 2 5.4 4.4 3 7.3 3c1.7 0 3.3.8 4.7 2 1.4-1.2 3-2 4.7-2C19.6 3 22 5.4 22 8.3c0 3.7-3.4 6.7-8.6 11.4z"/></svg></div><h4>Fried Calamari</h4><div class="price">$13</div><div class="stars">★★★★★</div><div class="add">ADD TO CART</div></div>
<div class="card" style="left:438px;top:2347px"><div class="dish" role="img" aria-label="Photo of a soft shell crab bun" style="background:radial-gradient(circle,#b0401a,#e8e0cc 55%,#bbb)"></div><div class="fav"><svg width="16" height="16" viewBox="0 0 24 24"><path fill="#999" d="M12 21l-1.4-1.3C5.4 15 2 12 2 8.3 2 5.4 4.4 3 7.3 3c1.7 0 3.3.8 4.7 2 1.4-1.2 3-2 4.7-2C19.6 3 22 5.4 22 8.3c0 3.7-3.4 6.7-8.6 11.4z"/></svg></div><h4>Soft Shell Crab</h4><div class="price">$15</div><div class="stars">★★★★★</div><div class="add">ADD TO CART</div></div>
<div class="card" style="left:777px;top:2347px"><div class="dish" role="img" aria-label="Photo of crispy chicken tenders with sauce" style="background:radial-gradient(circle,#d89030,#a06020 55%,#ddd)"></div><div class="fav"><svg width="16" height="16" viewBox="0 0 24 24"><path fill="#999" d="M12 21l-1.4-1.3C5.4 15 2 12 2 8.3 2 5.4 4.4 3 7.3 3c1.7 0 3.3.8 4.7 2 1.4-1.2 3-2 4.7-2C19.6 3 22 5.4 22 8.3c0 3.7-3.4 6.7-8.6 11.4z"/></svg></div><h4>Chicken Tenders (2pc)</h4><div class="price">$13</div><div class="stars">★★★★★</div><div class="add">ADD TO CART</div></div>
<div class="dots"><span class="on"></span><span></span><span></span><span></span></div>

<section>
  <div class="touch-photo" role="img" aria-label="Photo of glazed grilled crab in a white bowl"></div>
  <h2 class="title abs" style="left:620px;top:3260px;font-size:50px">Get In Touch</h2>
  <div class="rule" style="left:620px;top:3329px"></div>
  <div class="copy abs" style="left:621px;top:3363px;width:465px">
    <h3>Lorem ipsum dolor sit amet, consectetur adipiscing elit,</h3>
    <p>sed do eiusmod tempor incididunt ut labore et dolore magna aliqua. Ut enim ad minim veniam, quis nostrud exercitation ullamco laboris nisi ut aliquip ex ea commodo consequat. Duis aute irure dolor in reprehenderit in voluptate velit esse cillum dolore eu fugiat nulla pariatur. Excepteur sint occaecat cupidatat non proident, sunt in culpa qui officia deserunt mollit anim id est laborum.</p>
  </div>
  <div class="btn" style="left:622px;top:3608px;width:129px;height:43px;font-size:13px">Read More</div>
</section>

<footer class="footer"></footer>
<div class="brand" style="left:84px;top:4032px;font-size:17px;color:#fff;gap:8px"><span class="mark" style="width:26px;height:26px"></span>Lottie's Clam Shack</div>
<div class="social"><span></span><span></span><span></span><span></span></div>
<div class="fh" style="left:306px;top:3955px;color:#fff">Links</div>
<ul class="flinks" style="color:#fff"><li>Services</li><li>Industries</li><li>Request a Quote</li><li>About Us</li><li>Contact Us</li></ul>
<div class="fh" style="left:510px;top:3955px;color:#fff">Contact Us</div>
<div class="fitem" style="left:510px;top:4022px;color:#fff"><span class="ico"><svg width="16" height="16" viewBox="0 0 24 24"><path fill="#111" d="M12 2a7 7 0 0 0-7 7c0 5 7 13 7 13s7-8 7-13a7 7 0 0 0-7-7zm0 9.5A2.5 2.5 0 1 1 12 6a2.5 2.5 0 0 1 0 5.5z"/></svg></span><span>4820 Harbor Ln.<br>Westport, WA 98595</span></div>
<div class="fitem" style="left:510px;top:4085px;color:#fff"><span class="ico"><svg width="15" height="15" viewBox="0 0 24 24"><path fill="#111" d="M6.6 10.8a15 15 0 0 0 6.6 6.6l2.2-2.2c.3-.3.7-.4 1-.2 1.1.4 2.3.6 3.6.6.6 0 1 .4 1 1V20c0 .6-.4 1-1 1A17 17 0 0 1 3 4c0-.6.4-1 1-1h3.5c.6 0 1 .4 1 1 0 1.3.2 2.5.6 3.6.1.3 0 .7-.2 1z"/></svg></span>555-014-0273</div>
<div class="fitem" style="left:510px;top:4141px;color:#fff"><span class="ico"><svg width="15" height="15" viewBox="0 0 24 24"><path fill="#111" d="M3 6h18v12H3z"/><path d="M3 6l9 7 9-7" stroke="#fff" stroke-width="2" fill="none"/></svg></span>info@companyname.com</div>
<div class="fh" style="left:813px;top:3955px;color:#fff">Newsletter Sign Up</div>
<div class="abs" style="left:811px;top:4014px;font-size:14px;color:#fff">Sign up for free resources from our team.</div>
<div class="input">Enter e-mail address</div>
<div class="signup">SIGN UP NOW!</div>
<div class="next-spot"><b>Coming soon:</b> our second shack in Aberdeen, WA</div>
<div class="fbase"></div>

<div class="chat-widget" role="button" aria-label="Open contact and message widget">
  <svg width="24" height="24" viewBox="0 0 24 24"><path fill="#fff" d="M4 4h16a1 1 0 0 1 1 1v11a1 1 0 0 1-1 1H9l-5 4v-4H4a1 1 0 0 1-1-1V5a1 1 0 0 1 1-1z"/></svg>
</div>

</body>
</html>
```